Website front page and logo re-designed (using logo provided)

We are looking for the home page of our new website. It is a website offering a space for clients to ask professionals questions. The website should be similar in design to www.quibblenest.com however it is clear it should be a different look. It should be modern, simple to use, a clear navigation bar at the top and bottom.

Logo should be similar to the one attached, but more professional and modern. Logo should be clearly incorporated into website. Design should focus on our website colours as in the logo.

Logo Text

KnowHive - Truth with every reply!

Number of Pages Required

1 page

Font styles to use
Sans Serif

```html
<!DOCTYPE html>
<html lang="en">
<head>
<meta charset="utf-8">
<title>KnowHive - Truth with every reply!</title>
<link href="https://fonts.googleapis.com/css2?family=Roboto:ital,wght@0,400;0,500;0,700;1,400&display=swap" rel="stylesheet">
<style>
:root{
  --blue:#2f8fd8;
  --blue-dark:#1f7cc4;
  --red:#e8463a;
  --ink:#444;
  --muted:#666;
  --dark:#2b2b2b;
  --darker:#222;
  --line:#ddd;
}
*{box-sizing:border-box;margin:0;padding:0}
html,body{width:1200px;height:1200px;overflow:hidden;background:#fff;font-family:'Roboto',Arial,sans-serif;color:var(--ink)}
.page{position:absolute;left:236px;top:0;width:910px;height:1500px;transform:scale(.8);transform-origin:0 0}
.abs{position:absolute}
/* header */
.brand{left:183px;top:4px}
.brand-name{font-size:27px;font-weight:700;color:var(--blue);letter-spacing:-.5px;line-height:30px}
.brand-tag{font-size:10px;color:#222;margin-top:-1px}
.nav{left:380px;top:28px;display:flex;gap:14px;font-size:7px;color:#555;align-items:center}
.nav .home{width:10px;height:9px}
.contact-top{left:634px;top:6px;font-size:7px;color:var(--blue)}
.help{left:700px;top:3px;width:28px;height:13px;background:var(--red);color:#fff;font-size:7px;text-align:center;line-height:13px}
.search{left:613px;top:26px;width:102px;height:15px;border:1px solid #ccc}
.search-btn{left:714px;top:26px;width:15px;height:15px;background:var(--blue)}
.header-rule{left:0;top:48px;width:910px;height:2px;background:#e5e5e5}
/* hero */
.hero-photo{left:555px;top:52px;width:325px;height:316px;background:radial-gradient(ellipse at 45% 40%,#c9b7a6 0,#8a8f99 35%,#3c4452 60%,#e9edf2 85%,#fff 100%)}
.hero-side{left:880px;top:52px;width:30px;height:316px;background:#f3f3f3}
.hero-q{left:183px;top:72px;font-size:20px;font-weight:500;color:var(--blue)}
.hero-sub{left:183px;top:98px;font-size:19px;font-weight:500;color:#444}
.ask-box{left:182px;top:142px;width:383px;height:203px;background:var(--dark);border-radius:2px}
.tabs{left:188px;top:147px;display:flex;gap:8px;font-size:7px;color:#fff;align-items:center}
.tabs .on{background:var(--red);padding:3px 4px}
.ask-text{left:188px;top:167px;width:369px;height:95px;background:#fff;border-radius:2px}
.spec-label{left:300px;top:279px;font-size:8px;color:#fff}
.spec-select{left:431px;top:276px;width:126px;height:15px;background:#fff;font-size:6px;color:#666;padding:4px 6px}
.online{left:361px;top:314px;font-size:8px;color:#fff}
.btn{background:var(--blue);color:#fff;font-weight:500;text-align:center;border-radius:2px}
.hero-btn{left:457px;top:307px;width:100px;height:21px;font-size:10px;line-height:21px}
/* features */
.h2{width:910px;text-align:center;font-size:15px;font-weight:500;color:var(--blue)}
.feat{width:170px;text-align:center}
.feat svg{display:block;margin:0 auto}
.feat h3{font-size:11px;font-weight:400;color:#333;margin-top:6px}
.feat p{font-size:6px;color:#666;line-height:9px;margin-top:5px;text-transform:uppercase}
.start{left:581px;top:541px;width:122px;height:88px;border:1px solid var(--red)}
.start-head{height:27px;background:var(--red);color:#fff;font-size:14px;text-align:center;line-height:27px}
.start-btn{display:block;margin:19px auto 0;width:100px;height:21px;font-size:9px;line-height:21px}
/* band */
.band{left:0;top:654px;width:910px;height:220px;background:var(--blue)}
.band-title{left:0;top:676px;width:910px;text-align:center;color:#fff;font-size:14px;font-weight:500;line-height:17px}
.qtable{left:182px;top:732px;width:546px;border-collapse:collapse;font-size:6.5px;background:#fff}
.qtable th{background:var(--red);color:#fff;font-weight:400;height:23px;font-size:8.5px}
.qtable th:first-child{text-align:left;padding-left:9px;font-size:9px}
.qtable td{height:19px;border-bottom:1px solid #9cc6e9;color:#555;background:#f7f7f7}
.qtable td:first-child{padding-left:10px}
.qtable td.r{text-align:center;color:var(--red);font-size:8px;letter-spacing:1px}
.qtable td.r b{color:#444;font-weight:400}
.qtable td.d{text-align:center}
/* experts */
.expert{width:130px;text-align:center}
.avatar{width:74px;height:74px;border-radius:50%;margin:0 auto;border:2px solid var(--blue);background:radial-gradient(circle at 50% 45%,#c7a28a 0,#7a5a48 45%,#2f3a4a 100%)}
.stars{color:var(--red);font-size:8px;letter-spacing:2px;margin-top:10px}
.stars b{color:#444;font-weight:400}
.expert h4{font-size:9px;font-weight:500;color:var(--blue);margin-top:4px}
.expert p{font-size:6.5px;color:#555;line-height:9px;margin-top:4px}
.chev{stroke:#aaa;fill:none;stroke-width:1.5}
/* press */
.press{left:0;top:1096px;width:910px;height:51px;background:var(--blue);display:flex;justify-content:center;align-items:center;gap:42px;color:#dfeefa;font-size:13px;font-weight:700}
/* testimonial */
.testi{left:0;top:1147px;width:910px;height:187px;background:linear-gradient(90deg,#2e2e2e 0,#343434 55%,#2c3440 75%,#2e2e2e 100%)}
.quote-mark{left:208px;top:1198px;font-size:50px;color:#888;font-weight:700;line-height:40px}
.quote{left:205px;top:1231px;width:500px;text-align:center;color:#eee;font-style:italic;font-size:8.5px;line-height:14px}
.author{left:640px;top:1266px;color:#fff;font-size:9.5px;font-weight:500}
/* footer */
.strip{left:0;top:1333px;width:910px;height:22px;background:var(--red);color:#fff;font-size:7px}
.footer{left:0;top:1355px;width:910px;height:121px;background:var(--darker)}
.foot-contact-bg{left:602px;top:1355px;width:124px;height:121px;background:#1a1a1a}
.foot-logo{left:182px;top:1364px;width:117px;height:50px;background:#f2f2f2;padding:6px 7px}
.foot-logo .brand-name{font-size:22px;line-height:22px}
.foot-logo .brand-tag{font-size:9px}
.badge{left:182px;top:1417px;width:117px;height:50px;background:#f2f2f2}
.fcol h5{color:#fff;font-size:9px;font-weight:400;margin-bottom:6px}
.fcol li{list-style:none;color:#aaa;font-size:6.5px;line-height:14.5px;padding-left:5px}
.finfo{left:618px;top:1373px;width:110px;color:#bbb;font-size:6px;line-height:8.5px}
.finfo .row{display:flex;gap:6px;align-items:center;margin-top:4px}
.bottom{left:0;top:1476px;width:910px;height:24px;background:var(--blue);color:#fff;font-size:6px}
.social{left:628px;top:1483px;display:flex;gap:8px}
.social span{width:9px;height:9px;border-radius:50%;background:#fff;display:block}
</style>
</head>
<body>
<div class="page">
  <header>
    <div class="abs brand"><div class="brand-name">KnowHive</div><div class="brand-tag">Truth with every reply!</div></div>
    <nav class="abs nav">
      <svg class="home" viewBox="0 0 10 9"><path d="M5 0 0 4.5h1.5V9h2.5V6h2v3h2.5V4.5H10z" fill="#e8463a"/></svg>
      <span>How It Works</span><span>About Us</span><span>Browse</span><span>Login</span><span>Sign Up</span>
    </nav>
    <div class="abs contact-top">(140) 555-0182 or</div>
    <div class="abs help">Help</div>
    <div class="abs search"></div>
    <div class="abs search-btn"><svg width="15" height="15" viewBox="0 0 15 15"><circle cx="6.5" cy="6.5" r="3.5" stroke="#fff" stroke-width="1.4" fill="none"/><path d="M9 9l3.5 3.5" stroke="#fff" stroke-width="1.6"/></svg></div>
    <div class="abs header-rule"></div>
  </header>

  <section class="hero">
    <div class="abs hero-photo" role="img" aria-label="Portrait of a smiling grey-haired expert in a suit and tie"></div>
    <div class="abs hero-side"></div>
    <h1 class="abs hero-q">Have a Question?</h1>
    <p class="abs hero-sub">"Ask for expert Answers you can count on! "</p>
    <div class="abs ask-box"></div>
    <div class="abs tabs"><span class="on">Lawyers ▾</span><span>Mechanics</span><span>Doctors &amp; Nurses</span><span>Vets</span><span>Electricians &amp; Plumbers</span><span>Computer &amp; Education</span><span>MoreCategories</span></div>
    <div class="abs ask-text"></div>
    <div class="abs spec-label">Would you like to select a specialist:</div>
    <div class="abs spec-select">Optional<span style="float:right">▾</span></div>
    <div class="abs online">32 Experts are Online Now</div>
    <div class="abs btn hero-btn">Get an Answer</div>
  </section>

  <section class="why">
    <h2 class="abs h2" style="top:390px">Why ask a question ?</h2>
    <div class="abs feat" style="left:183px;top:437px">
      <svg width="32" height="30" viewBox="0 0 32 30"><path d="M16 2a6 6 0 0 0-6 6c0 5 6 11 6 11s6-6 6-11a6 6 0 0 0-6-6z" fill="none" stroke="#e8463a" stroke-width="2.4"/><circle cx="16" cy="8" r="2" fill="#e8463a"/><path d="M9 17 3 28h26l-6-11" fill="none" stroke="#e8463a" stroke-width="2.4"/></svg>
      <h3>Convenience</h3><p>Enjoy a fast, easy way to ask experts any-where you're online.</p>
    </div>
    <div class="abs feat" style="left:369px;top:433px">
      <svg width="32" height="34" viewBox="0 0 32 34"><path d="M13 18V4a2 2 0 0 1 4 0v10l7 2c2 .6 2 2 2 4v3c0 5-3 8-8 8h-2c-3 0-5-2-7-5l-3-5c-1-2 1-3 3-2l4 3z" fill="none" stroke="#e8463a" stroke-width="1.8"/></svg>
      <h3>One on one</h3><p>Enjoy a fast, easy way to ask experts any-where you're online.</p>
    </div>
    <div class="abs feat" style="left:555px;top:435px">
      <svg width="32" height="32" viewBox="0 0 32 32"><circle cx="16" cy="16" r="12" fill="none" stroke="#e8463a" stroke-width="2.6"/><circle cx="16" cy="16" r="7" fill="none" stroke="#e8463a" stroke-width="1.8"/><path d="M16 12v4h3" stroke="#e8463a" stroke-width="1.8" fill="none"/></svg>
      <h3>24/7 availability</h3><p>Enjoy a fast, easy way to ask experts any-where you're online.</p>
    </div>
    <div class="abs feat" style="left:183px;top:542px">
      <svg width="36" height="36" viewBox="0 0 36 36"><circle cx="16" cy="19" r="13" fill="none" stroke="#e8463a" stroke-width="2.6"/><circle cx="16" cy="19" r="7" fill="none" stroke="#e8463a" stroke-width="2.4"/><circle cx="16" cy="19" r="2" fill="#e8463a"/><path d="M16 19 30 5M27 3l5 0-2 5" stroke="#e8463a" stroke-width="2.2" fill="none"/></svg>
      <h3>Broad expertise</h3><p>Enjoy a fast, easy way to ask experts any-where you're online.</p>
    </div>
    <div class="abs feat" style="left:369px;top:542px">
      <svg width="36" height="36" viewBox="0 0 36 36"><circle cx="18" cy="18" r="15" fill="none" stroke="#e8463a" stroke-width="2.8"/><circle cx="13" cy="14" r="2" fill="#e8463a"/><circle cx="23" cy="14" r="2" fill="#e8463a"/><path d="M10 20q8 9 16 0" fill="none" stroke="#e8463a" stroke-width="2.6"/></svg>
      <h3>100% satisfaction</h3><p>Enjoy a fast, easy way to ask experts any-where you're online.</p>
    </div>
    <div class="abs start"><div class="start-head">Get Started</div><span class="btn start-btn">Get an Answer</span></div>
  </section>

  <section>
    <div class="abs band"></div>
    <h2 class="abs band-title">Join the 5 million people<br>who found a smarter way to get Expert help</h2>
    <table class="abs qtable">
      <tr><th>Recently answered questions</th><th style="width:90px">Rating</th><th style="width:90px">Date</th></tr>
      <tr><td>Lorem ipsum dolor sit amet, consectetur adipiscing elit. Quisque</td><td class="r">★★★★<b>★</b></td><td class="d">6 hours ago</td></tr>
      <tr><td>luctus nisi non augue consectetur, id elementum</td><td class="r">★★★★<b>★</b></td><td class="d">7 hours ago</td></tr>
      <tr><td>sodales eros urna, vitae elementum enim malesuada ut.</td><td class="r">★★★★<b>★</b></td><td class="d">8 hours ago</td></tr>
      <tr><td>Proin placerat commodo mattis. Pellentesque sit amet</td><td class="r">★★★★★</td><td class="d">9 hours ago</td></tr>
      <tr><td>Lorem ipsum dolor sit amet, consectetur adipiscing elit. Quisque</td><td class="r">★★★★<b>★</b></td><td class="d">10 hours ago</td></tr>
    </table>
  </section>

  <section class="experts">
    <h2 class="abs h2" style="top:896px">Our Experts</h2>
    <svg class="abs" style="left:180px;top:985px" width="14" height="38"><path class="chev" d="M12 1 2 19l10 18"/></svg>
    <svg class="abs" style="left:716px;top:985px" width="14" height="38"><path class="chev" d="M2 1l10 18L2 37"/></svg>
    <div class="abs expert" style="left:176px;top:935px"><div class="avatar" role="img" aria-label="Expert portrait"></div><div class="stars">★★★★<b>★</b></div><h4>Owen Draper, us</h4><p>consectetur adipiscing elit. Quisque luctus nisi non augue consectetur, id elementum nibh</p></div>
    <div class="abs expert" style="left:316px;top:935px"><div class="avatar" role="img" aria-label="Expert portrait"></div><div class="stars">★★★★<b>★</b></div><h4>Mr. Halvorsen, us</h4><p>consectetur adipiscing elit. Quisque luctus nisi non augue consectetur, id elementum nibh</p></div>
    <div class="abs expert" style="left:456px;top:935px"><div class="avatar" role="img" aria-label="Expert portrait"></div><div class="stars">★★★★<b>★</b></div><h4>Martin Ellery, us</h4><p>consectetur adipiscing elit. Quisque luctus nisi non augue consectetur, id elementum nibh</p></div>
    <div class="abs expert" style="left:596px;top:935px"><div class="avatar" role="img" aria-label="Expert portrait"></div><div class="stars">★★★★<b>★</b></div><h4>Clara Voss us</h4><p>consectetur adipiscing elit. Quisque luctus nisi non augue consectetur, id elementum nibh</p></div>
  </section>

  <div class="abs press"><span>Northbeam</span><span>Kestrel</span><span>The Harbor Ledger</span><span>Morning Lane</span><span>Ridge Journal</span></div>

  <section>
    <div class="abs testi" role="img" aria-label="Dimmed photo of a smiling technician in a navy work shirt"></div>
    <svg class="abs" style="left:182px;top:1218px" width="14" height="42"><path d="M12 1 2 21l10 20" stroke="#fff" stroke-width="1.5" fill="none"/></svg>
    <svg class="abs" style="left:714px;top:1218px" width="14" height="42"><path d="M2 1l10 20L2 41" stroke="#fff" stroke-width="1.5" fill="none"/></svg>
    <div class="abs quote-mark">“</div>
    <p class="abs quote">Morbi id lorem urna. Fusce nec ante eros. Aenean pharetra risus id ex dapibus commodo. Mauris imperdiet erat quis mattis ornare. Sed volutpat lorem eu risus rutrum ultricies. Ut ullamcorper urna ac interdum accumsan.</p>
    <div class="abs author">Peter Lindqvist.</div>
  </section>

  <footer>
    <div class="abs strip">
      <span class="abs" style="left:202px;top:5px;width:12px;height:12px;border-radius:50%;background:#fff"></span>
      <span class="abs" style="left:217px;top:7px">@knowhive: Fresh tips posted daily for every home question..</span>
      <span class="abs" style="left:617px;top:5px;font-size:8.5px">Contact Us</span>
    </div>
    <div class="abs footer"></div>
    <div class="abs foot-contact-bg"></div>
    <div class="abs foot-logo"><div class="brand-name">KnowHive</div><div class="brand-tag">Truth with every reply!</div></div>
    <div class="abs badge" role="img" aria-label="Satisfaction guarantee seal"><svg width="117" height="50"><rect x="25" y="12" width="67" height="26" rx="3" fill="#3a6fb0"/></svg></div>
    <div class="abs fcol" style="left:332px;top:1370px"><h5>Categories</h5><ul><li>About Us</li><li>Help FAQs</li><li>Our Promise</li><li>Login</li><li>Register</li></ul></div>
    <div class="abs fcol" style="left:475px;top:1370px"><h5>Useful Links</h5><ul><li>Careers</li><li>Become an Expert</li><li>Become an Affiliate</li><li>Refer an Expert</li></ul></div>
    <div class="abs finfo">
      <p>This is a short note about KnowHive. Proin gravida nibh vel velit auctor aliquet.</p>
      <div class="row" style="margin-top:9px"><svg width="6" height="8"><path d="M3 0a3 3 0 0 0-3 3c0 2 3 5 3 5s3-3 3-5a3 3 0 0 0-3-3z" fill="#bbb"/></svg>48 Alder Row, Fresno, USA</div>
      <div class="row"><svg width="6" height="6"><path d="M1 0h2l1 2-1 1 2 2 1-1 1 1v1c-4 0-6-2-6-6z" fill="#bbb"/></svg>+1 555 0147 / +1 555 0163</div>
      <div class="row"><svg width="7" height="5"><rect width="7" height="5" fill="#bbb"/></svg><span style="color:var(--blue)">hello@knowhive.example</span></div>
    </div>
    <div class="abs bottom"><span class="abs" style="left:182px;top:9px">Copyright 2016 KnowHive. All Rights Reserved.</span></div>
    <div class="abs social"><span></span><span></span><span></span><span></span><span></span></div>
  </footer>
</div>
</body>
</html>
```